Equine Podcast Cover Art Design

We need catchy cover art for a horse related podcast "Ride Onward Together"
Brief show description"
Whether you want to ride to experience horses, develop yourself to the next level as a horseman/horsewoman or ride to improve your physical and mental health, we are committed to helping you Ride Onward TogetherĀ®. Join us as we explore the nuance of equine management and sports as well as interview industry professionals to provide you with the knowledge necessary to be a better partner for your equine friends.
I have uploaded two existing logos we use for various purposes to give you an idea of existing style.
Target Market(s)
Horse owners and other equine professionals
Look and feel
Each slider illustrates characteristics of the customer's brand and the style your logo design should communicate.

```html
<!DOCTYPE html>
<html lang="en">
<head>
<meta charset="utf-8">
<title>Ride Onward Together — Podcast Cover</title>
<link rel="stylesheet" href="https://fonts.googleapis.com/css2?family=Stardos+Stencil:wght@700&family=Questrial&display=swap">
<style>
  :root {
    --forest-deep: #1f2a1c;
    --forest-mid: #4a4a2a;
    --amber-glow: #c8722a;
    --bark: #3a2414;
    --chestnut: #8a4a1e;
    --chestnut-dark: #4a2410;
    --headline: #ffffff;
    --tag-bg: #000000;
    --tag-text: #f5a800;
    --badge: #ffffff;
  }
  html, body {
    margin: 0;
    padding: 0;
    width: 1200px;
    height: 1200px;
    overflow: hidden;
    background: #1a1a1a;
  }
  .cover {
    position: relative;
    width: 1200px;
    height: 1200px;
    overflow: hidden;
  }
  .cover__backdrop {
    position: absolute;
    inset: 0;
    background:
      radial-gradient(ellipse 55% 50% at 95% 100%, rgba(230,140,60,0.85), transparent 70%),
      linear-gradient(90deg, rgba(0,0,0,0) 40%, rgba(60,40,20,0.35) 55%, rgba(0,0,0,0) 62%, rgba(40,30,15,0.4) 78%, rgba(0,0,0,0) 88%),
      linear-gradient(180deg, var(--forest-deep) 0%, var(--forest-mid) 35%, var(--bark) 70%, var(--amber-glow) 100%);
  }
  .cover__horse {
    position: absolute;
    left: 0;
    top: 10px;
    width: 560px;
    height: 1190px;
    border-radius: 48% 52% 0 0 / 22% 22% 0 0;
    background:
      radial-gradient(ellipse 40% 30% at 62% 62%, #1e1a1a 0%, transparent 70%),
      linear-gradient(180deg, var(--chestnut-dark) 0%, var(--chestnut) 40%, #b0602a 75%, var(--chestnut) 100%);
    opacity: 0.95;
  }
  .headline {
    position: absolute;
    right: 109px;
    top: 126px;
    margin: 0;
    font-family: "Stardos Stencil", "Impact", sans-serif;
    font-weight: 700;
    font-size: 92px;
    line-height: 108px;
    letter-spacing: 0.06em;
    color: var(--headline);
    text-align: right;
    text-transform: uppercase;
  }
  .headline__line { display: block; }
  .headline__mark {
    position: absolute;
    right: -52px;
    bottom: 64px;
    font-size: 40px;
    letter-spacing: 0;
  }
  .tagline {
    position: absolute;
    left: 555px;
    top: 607px;
    width: 555px;
    height: 160px;
    box-sizing: border-box;
    padding: 14px 31px 0 0;
    margin: 0;
    list-style: none;
    background: var(--tag-bg);
    text-align: right;
    font-family: "Questrial", "Century Gothic", sans-serif;
    font-size: 31px;
    line-height: 41px;
    letter-spacing: 0.04em;
    color: var(--tag-text);
  }
  .farm-name {
    position: absolute;
    left: 844px;
    top: 926px;
    width: 240px;
    text-align: center;
    font-family: "Questrial", "Century Gothic", sans-serif;
    color: var(--badge);
    text-transform: uppercase;
    font-size: 22px;
    line-height: 28px;
    letter-spacing: 0.08em;
  }
  .farm-name__dot {
    display: block;
    width: 22px;
    height: 22px;
    margin: 0 auto 12px;
    border: 3px solid var(--badge);
    border-radius: 50%;
  }
  .farm-name__place {
    display: block;
    margin-top: 6px;
    font-size: 13px;
    line-height: 18px;
    letter-spacing: 0.2em;
  }
</style>
</head>
<body>
  <main class="cover">
    <div class="cover__backdrop" role="img" aria-label="Blurred forest of tall tree trunks glowing in warm evening light"></div>
    <div class="cover__horse" role="img" aria-label="Chestnut horse with a white blaze wearing a dark leather halter, looking toward the viewer"></div>

    <h1 class="headline">
      <span class="headline__line">Ride</span>
      <span class="headline__line">Onward</span>
      <span class="headline__line">Together<span class="headline__mark">®</span></span>
    </h1>

    <ul class="tagline">
      <li>equine management</li>
      <li>equine sports</li>
      <li>better horsemanship</li>
    </ul>

    <div class="farm-name">
      <span class="farm-name__dot"></span>
      Steadfast Meadow Farm
      <span class="farm-name__place">Millbrook, Virginia</span>
    </div>
  </main>
</body>
</html>
```